KD Summit Fitness personal training needs a new Business Card design for 2016

Business Card design:
Our current business card is very plain
We are bringing on our first team member next year and thought its a perfect time to have a new face lift for our company!

We are a Personal Training business "KD Summit Fitness" who specializes in strength and conditioning / weightloss training,
We also run a yearly Bootcamp called "Ferocity Bootcamps", this is our Logo Design which we are looking for

The pink and blue in the logo are our business colours, how ever we don't want those colours to heavily dominate the card.

We are looking for a business card which is eye catching, and creative.

I am open to suggestions and any designs :)

Logo Design:

For our Logo Design we are looking for a bright, energetic logo, preferably a word logo which portrays strength and high intensity
If it has icon's etc in it thats fine again im open for suggestions :)
The Logo Design is for our Bootcamp which runs yearly
The bootcamp is called "Ferocity Bootcamp"

Target Market(s)

Age 20-40
Individuals who want to look great and have more energy

Industry/Entity Type

Business

Contact Information for Business Card

On the front
KD Summit Fitness Derwin Okoye Personal Training / Bootcamps / Pilates / Nutrition Healthy mind, Healthy body, Ultimate lifestyle < our slogan
Icons for the following
Email:
Mobile:
linkbook:
picstream:

On the back we would like to include somewhere
"Show this card to receive 50% off your first 30min pt session"
"Valid to one user only"

Logo Text

Ferocity Bootcamp

Font styles to use
Serif

Colors
e34197
0255a3
000000
ffffff

Requirements
Must have
• - Icons for picstream, linkbook, email and mobile phone
• - Slogan: Healthy mind, Healthy body, Ultimate lifestyle
• - What we offer: Personal Training , Bootcamps, Pilates, Nutrition
• - Logo
• -
Nice to have
• - Our 50% offer on the back
• - a place for a photo
Should not have
• - Pink and Blue everywhere

```html
<!DOCTYPE html>
<html lang="en">
<head>
<meta charset="utf-8">
<title>KD Summit Fitness – Business Card</title>
<link rel="stylesheet" href="https://fonts.googleapis.com/css2?family=Bebas+Neue&family=Montserrat:wght@500;600;700;800&display=swap">
<style>
  :root {
    --pink: #e34197;
    --blue: #2a4f9e;
    --black: #0b0b0c;
    --white: #ffffff;
    --ink: #1d1d1f;
    --muted: #4a4a4d;
    --stage: #3b3230;
    --photo-dark: #2b2c30;
    --photo-light: #c9b8aa;
  }
  * { box-sizing: border-box; margin: 0; padding: 0; }
  html, body {
    width: 1200px; height: 768px; overflow: hidden;
    background: var(--stage);
  }
  .stage { position: relative; width: 1200px; height: 768px; }
  .card {
    position: absolute; top: 232px;
    width: 530px; height: 303px;
    overflow: hidden;
    box-shadow: 0 10px 30px rgba(0,0,0,.45);
  }

  /* ---------- Back ---------- */
  .card-back { left: 40px; background: var(--black); color: var(--pink); }
  .offer {
    position: absolute; left: 55px; top: 80px; width: 420px;
    text-align: center;
    font-family: "Bebas Neue", sans-serif;
    font-size: 34px; line-height: 1.05; letter-spacing: .5px;
  }
  .offer-terms {
    position: absolute; left: 90px; top: 178px;
    font-family: "Montserrat", sans-serif; font-weight: 600;
    font-size: 10px; letter-spacing: .6px; text-transform: uppercase;
  }

  /* ---------- Front ---------- */
  .card-front {
    left: 630px; background: var(--white);
    font-family: "Montserrat", sans-serif; color: var(--ink);
  }
  .front-shapes { position: absolute; inset: 0; }
  .brand {
    position: absolute; left: 25px; top: 72px; width: 290px;
    text-align: center;
  }
  .brand-mark {
    width: 38px; height: 38px; border-radius: 50%;
    border: 4px solid var(--pink); margin: 0 auto 8px;
  }
  .brand-name {
    font-weight: 800; font-size: 22px; line-height: 1.1;
    color: var(--blue); text-transform: uppercase; white-space: nowrap;
  }
  .brand-slogan {
    margin-top: 6px; font-size: 8.5px; font-weight: 600; color: var(--muted);
    white-space: nowrap;
  }
  .person {
    position: absolute; right: 22px; top: 44px; text-align: right; color: var(--white);
  }
  .person-name { font-weight: 800; font-size: 18px; letter-spacing: 1px; text-transform: uppercase; }
  .person-role { font-weight: 500; font-size: 10px; line-height: 1.35; margin-top: 3px; }
  .photo {
    position: absolute; right: 24px; bottom: 0; width: 150px; height: 128px;
    background: linear-gradient(180deg, var(--photo-light) 0%, #a78f80 45%, var(--photo-dark) 70%);
    border-radius: 60px 60px 0 0;
  }
  .contacts { position: absolute; display: flex; flex-direction: column; gap: 8px; font-size: 11px; font-weight: 500; }
  .contacts-direct { left: 22px; top: 190px; }
  .contacts-social { left: 205px; top: 224px; }
  .contact { display: flex; align-items: center; gap: 7px; white-space: nowrap; }
  .contact svg { flex: none; }
  .contact .social-dot {
    width: 10px; height: 10px; border-radius: 50%;
    border: 1.5px solid var(--ink); flex: none;
  }
</style>
</head>
<body>
<main class="stage">

  <section class="card card-back" aria-label="Business card back">
    <p class="offer">Show this card to receive 50% off<br>your first 30min PT session</p>
    <p class="offer-terms">Valid to one user only</p>
  </section>

  <section class="card card-front" aria-label="Business card front">
    <svg class="front-shapes" width="530" height="303" viewBox="0 0 530 303" aria-hidden="true">
      <path d="M240 0 L530 0 L530 190 C470 150 420 150 380 160 C360 90 320 30 240 0 Z" fill="var(--blue)"/>
      <path d="M0 40 C70 8 170 -2 250 6 C320 14 370 60 395 120 C360 55 300 22 230 18 C150 14 70 26 0 52 Z" fill="var(--pink)"/>
    </svg>

    <div class="brand">
      <div class="brand-mark"></div>
      <p class="brand-name">KD Summit Fitness</p>
      <p class="brand-slogan">Healthy mind, Healthy body, Ultimate lifestyle</p>
    </div>

    <div class="person">
      <p class="person-name">Derwin Okoye</p>
      <p class="person-role">Personal Training , Bootcamps<br>Pilates, Nutrition</p>
    </div>

    <div class="photo" role="img" aria-label="Portrait photo of the trainer"></div>

    <div class="contacts contacts-direct">
      <p class="contact">
        <svg width="9" height="12" viewBox="0 0 9 12" aria-hidden="true"><rect x="0.5" y="0.5" width="8" height="11" rx="1.5" fill="none" stroke="var(--ink)"/><circle cx="4.5" cy="9.5" r=".9" fill="var(--ink)"/></svg>
        +00 111 222 3333
      </p>
      <p class="contact">
        <svg width="12" height="9" viewBox="0 0 12 9" aria-hidden="true"><rect x=".5" y=".5" width="11" height="8" fill="none" stroke="var(--ink)"/><path d="M.5 .5 L6 5 L11.5 .5" fill="none" stroke="var(--ink)"/></svg>
        yourname@yourwebsite.com
      </p>
    </div>

    <div class="contacts contacts-social">
      <p class="contact"><span class="social-dot"></span>linkbook@yourname</p>
      <p class="contact"><span class="social-dot"></span>picstream@yourname</p>
    </div>
  </section>

</main>
</body>
</html>
```